Emergency Dental Referral Company

I need a brochure to advertise my business to prospective dentists that may want to join or to dentists that may want to use this for their own patients. I also need to advertise this brochure to ER physicians who see many dental emergencies. This brochure is meant to be dual purpose: advertise our company and services to the ER physicians who then hand out the brochures to the dental emergency patients in pain. See our website for further details at www.molarquickfix.com

I will also be attaching our logo design.

Target Market(s)

Emergency Room physicians and other medical personnel who will distribute these brochures to patients in dental pain and dental emergencies

Industry/Entity Type

Business

Font styles to use
Serif
Sans Serif

Requirements
Must have
• Must be simple! Must have a call to action- inspiration to go to website. Highlight our guarantee that states "If you are not seen by a dentist in 24 hours or less, you will receive your money back. Emphasis on the logo. Must discuss how we find a dentist in your zip code in three easy steps.
• For the color- please make similar to our website of www.molarquickfix.com
Nice to have
• Would like to state that this service can see patients at any hour of the day.
Should not have
• no contact information besides the URL. www.molarquickfix.com

```html
<!DOCTYPE html>
<html lang="en">
<head>
<meta charset="utf-8">
<title>Molar Quick Fix – Brochure</title>
<link href="https://fonts.googleapis.com/css2?family=Oswald:wght@500;700&family=Roboto+Condensed:wght@400;700&family=Montserrat:wght@700&display=swap" rel="stylesheet">
<style>
  :root {
    --brand-blue: #1f73bd;
    --brand-blue-dark: #17609f;
    --brand-green: #1f9a3e;
    --paper: #ffffff;
    --paper-tint: #eef4fa;
    --stage: #e4e5e7;
    --ink-grey: #555a60;
    --photo-light: #d9d4cf;
    --photo-dark: #8a7a70;
  }
  * { margin: 0; padding: 0; box-sizing: border-box; }
  html, body { width: 1200px; height: 845px; overflow: hidden; background: var(--stage); }
  .canvas { position: relative; width: 1200px; height: 845px; }

  .panel {
    position: absolute; top: 40px; width: 570px; height: 765px;
    background: linear-gradient(160deg, var(--paper) 0%, var(--paper-tint) 55%, var(--paper) 100%);
    overflow: hidden;
  }
  .panel--front-left { left: 30px; }
  .panel--front-right { left: 600px; border-left: 1px solid #d6dbe0; }

  /* Left panel */
  .headline-band {
    position: absolute; top: 40px; left: 0; width: 100%; height: 92px;
    background: var(--brand-blue);
    font-family: "Oswald", sans-serif; font-weight: 500; color: var(--paper);
    font-size: 62px; line-height: 92px; padding-left: 48px; letter-spacing: 0.5px;
  }
  .headline-accent {
    position: absolute; top: 140px; left: 200px;
    font-family: "Oswald", sans-serif; font-weight: 700; color: var(--brand-green);
    font-size: 64px; line-height: 1; letter-spacing: 1px;
  }
  .mission {
    position: absolute; top: 250px; left: 48px; width: 150px;
    font-family: "Roboto Condensed", sans-serif; font-weight: 700; color: var(--brand-blue);
    font-size: 23px; line-height: 1.18; text-align: center;
  }
  .hero-photo {
    position: absolute; top: 235px; left: 215px; width: 325px; height: 275px;
    background: linear-gradient(135deg, var(--photo-dark) 0%, var(--photo-light) 60%, #f2efec 100%);
  }
  .url-band {
    position: absolute; left: 0; width: 100%; height: 70px;
    background: var(--brand-blue); color: var(--paper);
    font-family: "Roboto Condensed", sans-serif; font-weight: 700;
  }
  .panel--front-left .url-band {
    bottom: 60px; font-size: 34px; line-height: 70px; padding-left: 235px;
  }
  .guarantee-badge {
    position: absolute; left: 20px; bottom: 20px; width: 200px; height: 170px;
    background: var(--brand-green); color: var(--paper);
    font-family: "Montserrat", sans-serif; font-weight: 700; text-align: center;
    display: flex; flex-direction: column; justify-content: center; line-height: 1.1;
  }
  .guarantee-badge .small { font-size: 19px; }
  .guarantee-badge .big { font-size: 34px; }
  .guarantee-badge .tiny { font-size: 14px; }

  /* Right panel */
  .brand-lockup {
    position: absolute; top: 60px; left: 0; width: 100%;
    display: flex; align-items: center; justify-content: center; gap: 16px;
  }
  .brand-mark { width: 34px; height: 34px; border-radius: 50%; background: var(--brand-blue); }
  .brand-name {
    font-family: "Roboto Condensed", sans-serif; font-weight: 700;
    font-size: 50px; color: var(--brand-blue);
  }
  .steps-title {
    position: absolute; top: 225px; left: 0; width: 100%;
    display: flex; justify-content: center; align-items: center; gap: 10px;
    font-family: "Roboto Condensed", sans-serif; font-weight: 700; color: var(--brand-blue);
  }
  .steps-title .count { font-size: 96px; color: var(--brand-green); line-height: 1; }
  .steps-title .words { font-size: 32px; line-height: 1.1; }
  .steps {
    position: absolute; top: 385px; left: 0; width: 100%;
    display: flex; justify-content: center; gap: 14px; list-style: none;
  }
  .step {
    width: 150px; height: 120px; border-radius: 50%;
    background: var(--brand-blue); color: var(--paper);
    font-family: "Roboto Condensed", sans-serif; text-align: center;
    display: flex; flex-direction: column; justify-content: center;
  }
  .step .label { font-weight: 700; font-size: 20px; }
  .step .action { font-size: 17px; margin-top: 6px; line-height: 1.1; }
  .panel--front-right .url-band {
    top: 540px; text-align: center; font-size: 40px; line-height: 70px;
  }
  .fine-guarantee {
    position: absolute; top: 622px; left: 0; width: 100%; text-align: center;
    font-family: "Roboto Condensed", sans-serif; font-weight: 700;
    color: var(--brand-green); font-size: 16px; line-height: 1.25;
  }
  .fine-guarantee strong { font-size: 20px; }
</style>
</head>
<body>
<main class="canvas">
  <section class="panel panel--front-left">
    <h1 class="headline-band">Get you out of</h1>
    <div class="headline-accent">PAIN</div>
    <p class="mission">Our mission plain is to get you seen by a qualified dentist as quickly as possible to get you out of pain</p>
    <div class="hero-photo" role="img" aria-label="Photo of a smiling patient in a dental chair"></div>
    <div class="url-band">www.molarquickfix.com</div>
    <div class="guarantee-badge">
      <span class="small">Get seen within</span>
      <span class="big">24 hours</span>
      <span class="tiny">or your</span>
      <span class="small">money back!</span>
    </div>
  </section>

  <section class="panel panel--front-right">
    <div class="brand-lockup">
      <span class="brand-mark"></span>
      <span class="brand-name">Molar Quick Fix</span>
    </div>
    <h2 class="steps-title">
      <span class="count">3</span>
      <span class="words">Your dentist is<br>easy steps<br>away</span>
    </h2>
    <ol class="steps">
      <li class="step"><span class="label">Step 1</span><span class="action">Fill out a Form</span></li>
      <li class="step"><span class="label">Step 2</span><span class="action">Find a Dentist</span></li>
      <li class="step"><span class="label">Step 3</span><span class="action">Get your<br>appointment</span></li>
    </ol>
    <div class="url-band">www.molarquickfix.com</div>
    <p class="fine-guarantee">If you are not seen by a dentist in <strong>24</strong> hours<br>or less, you will receive your money back</p>
  </section>
</main>
</body>
</html>
```